Business card for home developer

Name, email, phone #, logo, address, lic # and slogan.
Slogan to say something like, "Leader in quality neighborhood communities" maybe? The last one said "A sept above the rest". Some thing saying we are above the other people.
Updates
The card can be two sided?
Target Market(s)
Home buyers
Industry/Entity Type
Business
Look and feel
Each slider illustrates characteristics of the customer's brand and the style your logo design should communicate.

```html
<!DOCTYPE html>
<html lang="en">
<head>
<meta charset="utf-8">
<title>Business Card – Crestline Homes</title>
<link rel="stylesheet" href="https://fonts.googleapis.com/css2?family=Lato:ital,wght@0,400;0,700;0,900;1,400&display=swap">
<style>
  :root {
    --backdrop: #6f6f6f;
    --card-white: #ffffff;
    --brand-blue: #27407f;
    --brand-red: #c1272d;
    --text-light: #ffffff;
  }
  * { margin: 0; padding: 0; box-sizing: border-box; }
  html, body {
    width: 1200px;
    height: 900px;
    overflow: hidden;
    background: var(--backdrop);
    font-family: "Lato", Arial, sans-serif;
  }
  .canvas {
    position: relative;
    width: 1200px;
    height: 900px;
    display: flex;
    align-items: center;
    justify-content: center;
  }
  .business-card {
    position: relative;
    width: 1000px;
    height: 572px;
    background: var(--card-white);
    overflow: hidden;
    box-shadow: 0 10px 30px rgba(0,0,0,0.25);
  }
  .card-header {
    position: absolute;
    left: 0; top: 0;
    width: 100%;
    height: 218px;
    display: flex;
    align-items: center;
    justify-content: space-between;
    padding: 0 70px 0 72px;
  }
  .person-name {
    font-size: 42px;
    font-weight: 400;
    color: var(--brand-blue);
    letter-spacing: 0.2px;
    margin-top: -14px;
  }
  .person-name strong { font-weight: 700; }
  .company-mark {
    display: flex;
    align-items: center;
    gap: 16px;
    margin-top: -6px;
  }
  .company-mark .mark-dot {
    width: 54px;
    height: 54px;
    border-radius: 50%;
    background: var(--brand-red);
    flex: none;
  }
  .company-name {
    font-size: 50px;
    font-weight: 900;
    color: var(--brand-blue);
    letter-spacing: 1px;
    text-transform: uppercase;
    line-height: 1;
  }
  .slogan-band {
    position: absolute;
    left: 0; top: 218px;
    width: 100%;
    height: 36px;
    background: var(--brand-red);
    color: var(--text-light);
    font-size: 21px;
    font-weight: 700;
    letter-spacing: 4px;
    text-transform: uppercase;
    line-height: 36px;
    padding-left: 72px;
    white-space: nowrap;
  }
  .contact-panel {
    position: absolute;
    left: 0; top: 254px;
    width: 100%;
    height: 318px;
    background: var(--brand-blue);
    padding: 44px 0 0 72px;
  }
  .contact-list {
    list-style: none;
    color: var(--text-light);
    font-size: 27px;
    line-height: 45px;
  }
  .contact-list .label { font-style: italic; }
</style>
</head>
<body>
  <main class="canvas">
    <article class="business-card">
      <header class="card-header">
        <h1 class="person-name">John <strong>Smith</strong></h1>
        <div class="company-mark">
          <span class="mark-dot" aria-hidden="true"></span>
          <span class="company-name">Crestline Homes</span>
        </div>
      </header>
      <p class="slogan-band">Leader in Quality Neighborhood Communities</p>
      <section class="contact-panel">
        <ul class="contact-list">
          <li><span class="label">phone:</span> 123-456-7890</li>
          <li><span class="label">web:</span> yourdomain.com</li>
          <li><span class="label">email:</span> yourname@yourdomain.com</li>
          <li><span class="label">lic:</span> #123 456</li>
          <li><span class="label">address:</span> Street address goes here, Suite #303, Alt Bldg, NY 82365</li>
        </ul>
      </section>
    </article>
  </main>
</body>
</html>
```